P&H RESTORATION

I want a brochure similiar to the example i've attached.
My company name is P&H Restoration. The website is: P-H-Restoration.com.
The phone number is 803.417.9056.

I don't like the "yellow" being the main color of the example so I'm open to suggestions. I want something CLEAN & Simple, like our logo . This will be a bi fold brochure

```html
<!DOCTYPE html>
<html lang="en">
<head>
<meta charset="utf-8">
<title>P&amp;H Restoration – Brochure Cover</title>
<link rel="stylesheet" href="https://fonts.googleapis.com/css2?family=Poppins:wght@300;400;500&display=swap">
<style>
  :root {
    --paper: #ffffff;
    --charcoal-light: #4f4f4e;
    --charcoal-dark: #262626;
    --lime: #8dc63f;
    --lime-light: #b4e35a;
    --lime-dark: #6f9f2a;
    --ink-light: #ffffff;
  }
  html, body {
    margin: 0;
    padding: 0;
    overflow: hidden;
    background: var(--paper);
  }
  .cover {
    position: relative;
    width: 848px;
    height: 1200px;
    overflow: hidden;
    background: var(--paper);
    font-family: "Poppins", sans-serif;
  }
  .cover__shapes {
    position: absolute;
    inset: 0;
  }
  .brand {
    position: absolute;
    left: 0;
    right: 0;
    top: 545px;
    text-align: center;
    color: var(--ink-light);
    font-weight: 300;
    font-size: 58px;
    letter-spacing: 1px;
    line-height: 1;
    margin: 0;
  }
  .tagline {
    position: absolute;
    left: 72px;
    top: 908px;
    margin: 0;
    font-weight: 500;
    font-size: 33px;
    line-height: 54px;
    letter-spacing: 0.5px;
  }
  .tagline__question { display: block; color: var(--ink-light); }
  .tagline__answer { display: block; color: var(--lime); }
  .contact {
    position: absolute;
    left: 72px;
    top: 1058px;
    margin: 0;
    padding: 0;
    list-style: none;
    color: var(--ink-light);
    font-weight: 400;
    font-size: 29px;
  }
  .contact__item {
    display: flex;
    align-items: center;
    gap: 16px;
    height: 52px;
  }
  .contact__icon { width: 30px; height: 30px; flex: none; }
</style>
</head>
<body>
<main class="cover">
  <svg class="cover__shapes" width="848" height="1200" viewBox="0 0 848 1200">
    <defs>
      <linearGradient id="blueprint-tone" x1="0" y1="0" x2="0.3" y2="1">
        <stop offset="0" stop-color="var(--charcoal-light)"/>
        <stop offset="0.6" stop-color="var(--charcoal-dark)"/>
        <stop offset="1" stop-color="#3a3a3a"/>
      </linearGradient>
      <linearGradient id="interior-tone" x1="0" y1="0" x2="0" y2="1">
        <stop offset="0" stop-color="var(--lime-light)"/>
        <stop offset="1" stop-color="var(--lime-dark)"/>
      </linearGradient>
    </defs>
    <polygon class="blueprint-panel" role="img" aria-label="Rolled architectural blueprints photographed in grey tones"
             points="118,0 848,0 848,606 538,1200 0,1200 0,226" fill="url(#blueprint-tone)"/>
    <polygon class="interior-panel" role="img" aria-label="Room under renovation with a step ladder, tinted green"
             points="848,606 848,1200 538,1200" fill="url(#interior-tone)"/>
  </svg>

  <h1 class="brand">P&amp;H Restoration</h1>

  <h2 class="tagline">
    <span class="tagline__question">INSURANCE CLAIM?</span>
    <span class="tagline__answer">WE'RE ON YOUR TEAM.</span>
  </h2>

  <ul class="contact">
    <li class="contact__item">
      <svg class="contact__icon" viewBox="0 0 30 30" aria-hidden="true">
        <circle cx="15" cy="15" r="13" fill="none" stroke="var(--lime)" stroke-width="3"/>
        <ellipse cx="15" cy="15" rx="5.5" ry="13" fill="none" stroke="var(--lime)" stroke-width="2"/>
        <line x1="2" y1="15" x2="28" y2="15" stroke="var(--lime)" stroke-width="2"/>
      </svg>
      <span>P-H-Restoration.com</span>
    </li>
    <li class="contact__item">
      <svg class="contact__icon" viewBox="0 0 24 24" aria-hidden="true">
        <path fill="var(--lime)" d="M6.6 10.8c1.4 2.8 3.8 5.1 6.6 6.6l2.2-2.2c.3-.3.7-.4 1-.2 1.1.4 2.3.6 3.6.6.6 0 1 .4 1 1V20c0 .6-.4 1-1 1C10.6 21 3 13.4 3 4c0-.6.4-1 1-1h3.5c.6 0 1 .4 1 1 0 1.3.2 2.5.6 3.6.1.3 0 .7-.2 1l-2.3 2.2z"/>
      </svg>
      <span>803.417.9056</span>
    </li>
  </ul>
</main>
</body>
</html>
```